Brochure Design Project

Designers,

We are a Refinery and we want to create a brochure. Our name is Lindell Bullion Works aka Lindell BWR. This brochure will aid in selling and acquiring new clients. We will literally use this as a tool to go by as we explain who we are to our clients.

We have already made a brochure and would like you to build off of it. What I mean by this is, take the exact wording and pictures and stick to the story line. I want to see your ideas for a brochure design but copy and paste the story line. The only exception that we want to see is the front page; I want to see new pictures for the front fold. But by all means change color, designs, fonts, watermarks, etc. the only thing that I ask is stay with the story line. We have structured the presentation a specific way that will aid us in selling our company.
Updates

Designers,

I have changed the whole plan, I Realized that many have misunderstood what I was explaining. But I created a solution. I originally wanted people to follow the story line in the “brochure_black” and take ideas from both brochures. But I saw that wasn’t the case. So I redid the “brochure_black” and put the actually photos in the new brochure. What I want is for everyone to use the story line that I created with the brochure, copy and paste all the photos and wording. I have deleted all the brochures and only put up one file. I ask that everyone downloads the new file and start fresh. Like I said before, I want to see new ideas like the design, font, colors, textures, gadgets etc. but I want everyone to stay to the story line I created. The only exception that we want to see is the front page; I want to see new pictures for the front fold. I love all the designs that have been submitted, but what I noticed none of them followed the story line.

I have posted the new set of photos on dropbox. the Account user name is lindellbwr@mailbrook.example
Password:Folder58sketches

I have posted the new brochure file as PDF also

Thank you

I have posted a new picture that will replace the waiting room photo on the transparency point. please make the changes accordingly.

thank you all for your posts and updated brochures. I want to reconfirm that i have uploaded a new photo for the waiting room. please replace the old photo with this photo. if you have any questions please contact me. 

Industry/Entity Type

It Company

Requirements
Must have
• We like

```html
<!DOCTYPE html>
<html lang="en">
<head>
<meta charset="utf-8">
<title>Lindell BWR Brochure</title>
<link href="https://fonts.googleapis.com/css2?family=Oswald:wght@400;600;700&family=Open+Sans:ital,wght@0,400;0,600;1,400&display=swap" rel="stylesheet">
<style>
:root{
  --gold:#e9a01b;
  --gold-deep:#b9770d;
  --ink:#1a1a1a;
  --text:#3a3a3a;
  --paper:#ffffff;
  --canvas:#e6e6e6;
  --map:#cfd2d4;
}
*{margin:0;padding:0;box-sizing:border-box}
html,body{width:851px;height:1200px;overflow:hidden;background:var(--canvas)}
body{position:relative;font-family:"Open Sans",Arial,sans-serif;color:var(--text)}
.spread{position:absolute;left:0;width:851px;height:596px;background:var(--paper)}
.spread.outside{top:0}
.spread.inside{top:604px}
.panel{position:absolute;top:0;height:100%;width:283px;overflow:hidden}
.p1{left:0}.p2{left:284px}.p3{left:568px}
.photo{position:absolute}
.body-copy{position:absolute;font-size:7.6px;line-height:1.5}
.body-copy p{margin-bottom:9px}
.signature{font-size:7.6px;line-height:1.5}
.dark{background:var(--ink)}
.tiles{position:absolute;display:flex;flex-direction:column;gap:10px}
.tile{width:36px;height:38px;border:2px solid var(--gold);color:var(--gold);font-family:"Oswald",sans-serif;font-size:17px;display:flex;align-items:center;justify-content:center;background:rgba(0,0,0,.15)}
.brand{position:absolute;right:14px;top:16px;text-align:right;color:#fff}
.brand-name{font-family:"Oswald",sans-serif;font-weight:600;font-size:20px;letter-spacing:.5px}
.brand-sub{font-size:5.5px;letter-spacing:1.4px;color:#bbb;text-transform:uppercase}
.headline{position:absolute;left:30px;top:300px;width:240px;text-align:right;color:var(--gold);font-family:"Oswald",sans-serif}
.headline .big{font-size:58px;font-weight:700;font-style:italic;line-height:1;letter-spacing:2px}
.headline .small{font-size:14px;font-weight:600;letter-spacing:2px;margin-top:2px}
.headline .tag{font-family:"Open Sans",sans-serif;font-style:italic;font-size:10px;color:#ddd;margin-top:14px;line-height:1.4}
.map{position:absolute;left:0;top:192px;width:283px;height:228px;background:linear-gradient(135deg,#d9dbdc,#bfc3c5)}
.address-box{position:absolute;left:14px;top:40px;width:98px;height:116px;background:var(--ink);color:#fff;padding:8px;font-size:5.4px;line-height:1.5}
.address-box strong{display:block;font-size:7px;margin-bottom:8px}
.pin{position:absolute;left:170px;top:96px}
</style>
</head>
<body>

<section class="spread outside">
  <div class="panel p1">
    <div class="photo" role="img" aria-label="Photo of a bright office interior with a doorway" style="left:10px;top:10px;width:263px;height:150px;background:linear-gradient(160deg,#d8cdb8,#8a7c66 60%,#3e3a34)"></div>
    <div class="body-copy" style="left:14px;top:182px;width:250px">
      <p>“Lindell Bullion Works Refinery Inc. is the most accommodating refinery I have ever dealt with... and never any unexpected charges or hidden fees. As if they can do it my scrap bill be any business, I don't like watches.</p>
      <p>With Lindell Bullion Works Refinery I get the most out of my precious metals, fast turn around and competent personal service.”</p>
      <p class="signature">Rory “Hammer” Feldt<br>owner of Cobalt Gem Exchange, Portland, OR</p>
    </div>
  </div>

  <div class="panel p2">
    <div class="photo dark" style="left:0;top:0;width:283px;height:192px">
      <div role="img" aria-label="Photo of refined gold on a workbench" style="position:absolute;left:10px;top:10px;width:263px;height:172px;background:linear-gradient(150deg,#e2c785,#a97a2a 45%,#3a2a12)"></div>
    </div>
    <div class="map" role="img" aria-label="Street map showing the refinery location">
      <div class="address-box">
        <strong>Lindell Bullion Works Refinery, Inc.</strong>
        2840 Harlow Ave NE<br>Suite 12<br>Salem, OR 97301<br><br>Phone: (555) 014-2287<br>Mon – Fri 9am – 5pm
      </div>
      <svg class="pin" width="18" height="24" viewBox="0 0 18 24"><path d="M9 0C4 0 0 4 0 9c0 7 9 15 9 15s9-8 9-15c0-5-4-9-9-9z" fill="#c0392b"/><circle cx="9" cy="9" r="3.5" fill="#fff"/></svg>
    </div>
  </div>

  <div class="panel p3 dark">
    <div class="brand">
      <div class="brand-name">Lindell BWR</div>
      <div class="brand-sub">Lindell Bullion Works Refinery</div>
    </div>
    <div class="photo" role="img" aria-label="Close-up photo of crumpled gold leaf" style="left:0;top:56px;width:232px;height:226px;background:linear-gradient(135deg,#f3d27a,#c78a1e 45%,#6a4306 80%,#2a1a05)"></div>
    <div class="tiles" style="left:240px;top:60px">
      <div class="tile">Au</div><div class="tile">Ag</div><div class="tile">Pt</div><div class="tile">Rh</div>
    </div>
    <div class="headline">
      <div class="big">TRUST</div>
      <div class="small">THROUGH TRANSPARENCY</div>
      <div class="tag">Handling your precious<br>metals with precision and care.</div>
    </div>
  </div>
</section>

<section class="spread inside">
  <div class="panel p1">
    <div class="photo" role="img" aria-label="Photo of the refinery lab with stainless steel equipment" style="left:10px;top:10px;width:263px;height:190px;background:linear-gradient(160deg,#c9c9c6,#7d7b74 55%,#2f2d2a)"></div>
    <div class="body-copy" style="left:14px;top:216px;width:250px">
      <p>Established in 2009, Lindell Bullion Works (LBW) has been serving the greater Northwest region with precious metals smelting and refining.</p>
      <p>Located in Salem, Oregon, LBW strives to build a positive relationship with our clients through transparency, accuracy and high customer service... making your refining experience the best it can be.</p>
      <p>To build trust with our clients, LBW has a transparent policy. We do not hide anything from our clients.</p>
      <p>For more information or to schedule an appointment, call (555) 014-2287 or email lindellbwr@mailbrook.example</p>
    </div>
  </div>

  <div class="panel p2">
    <div class="photo" role="img" aria-label="Photo of the refinery floor with furnaces and workstations" style="left:0;top:0;width:283px;height:280px;background:linear-gradient(170deg,#dcdcda,#9c9a95 50%,#4a4844)"></div>
    <div class="body-copy" style="left:14px;top:302px;width:255px">
      <p>From the moment your metals exchange hands you will be able to view the smelting process from the weigh in to when the bar is poured and assayed. With our trade certified scales and commercial grade assay machine we are able to guarantee you get the most accurate assessment of your metals.</p>
      <p>In an industry that is full of doubt and scams, LBW has found that integrity and trust goes a long way. These values are what our company was founded on and are at the core of how we conduct business.</p>
    </div>
  </div>

  <div class="panel p3">
    <div class="photo" role="img" aria-label="Photo of the client waiting room" style="left:6px;top:10px;width:232px;height:180px;background:linear-gradient(160deg,#e0d6c4,#a0917a 55%,#4d4436)"></div>
    <div class="tiles" style="left:238px;top:200px">
      <div class="tile">Au</div><div class="tile">Ag</div><div class="tile">Pt</div><div class="tile">Rh</div>
    </div>
    <div class="body-copy" style="left:30px;top:200px;width:195px">
      <p>“We have been doing business with Lindell Bullion Works Refinery for over a year or so, and have been very pleased with the honesty and fair pricing that the company has given to us. The facility that they provide is very friendly and safe. You can view your refining if you wish and see the process done from start to finish. They are very fast and very reliable, and we like doing business with them.”</p>
      <p class="signature">Marco Vesely</p>
    </div>
  </div>
</section>

</body>
</html>
```